Design for Chirpwall Ad to promote Laptops purchase

Need a graphic design for a Chirpwall Ad - to promote 2 laptops (PC and Zorvane) with the stated required ad-text.

AD TEXT:

FOR SME BUSINESS ONLY!
Chat with us!
To get advice on how to apply
and defray up to 80%* of business laptop purchase cost!

*Terms and Conditions apply

Image for reference only

Target Market(s)

Small medium business

Font styles to use
Sans Serif

Requirements
Must have
• 2 laptop images (see attached ) - 1 vector image of ZORVANE , and pls try to create another vector image of PC laptop (where screen is showing Blue Pendrel screen)

```html
<!DOCTYPE html>
<html lang="en">
<head>
<meta charset="utf-8">
<title>SME Business Laptop Ad</title>
<link rel="stylesheet" href="https://fonts.googleapis.com/css2?family=Montserrat:ital,wght@0,400;0,700;0,800;1,700&display=swap">
<style>
  :root {
    --teal: #43cbb9;
    --yellow: #f3da35;
    --frame-tint: rgba(255, 255, 255, 0.22);
    --red: #e31e24;
    --red-dark: #a51c1f;
    --ink: #1f1f1f;
    --bubble-grey: #3f3f3f;
    --white: #ffffff;
  }
  html, body {
    margin: 0;
    padding: 0;
    overflow: hidden;
  }
  .ad {
    position: relative;
    width: 1200px;
    height: 1200px;
    overflow: hidden;
    font-family: "Montserrat", sans-serif;
    color: var(--ink);
  }
  .ad__backdrop {
    position: absolute;
    inset: 0;
  }
  .laptop {
    position: absolute;
    border-radius: 14px;
  }
  .laptop--pc {
    left: 588px;
    top: 124px;
    width: 572px;
    height: 388px;
    background: linear-gradient(160deg, #1fa6e6 0%, #2aa7e4 45%, #bfc3c8 70%, #9ea3a8 100%);
  }
  .laptop--zorvane {
    left: 36px;
    top: 140px;
    width: 728px;
    height: 424px;
    background: linear-gradient(180deg, #1d1d1f 0%, #1f8fe0 8%, #1a86dc 80%, #cfd2d5 94%, #a9adb1 100%);
  }
  .ribbon {
    position: absolute;
    left: 0;
    top: 0;
  }
  .ribbon__text {
    position: absolute;
    left: 200px;
    width: 798px;
    top: 627px;
    margin: 0;
    font-size: 52px;
    line-height: 1;
    font-weight: 700;
    color: var(--white);
    text-align: center;
    white-space: nowrap;
    letter-spacing: -1px;
  }
  .chat-icon {
    position: absolute;
    left: 508px;
    top: 732px;
  }
  .headline, .body-line, .footnote {
    position: absolute;
    margin: 0;
    line-height: 1;
    white-space: nowrap;
  }
  .headline {
    left: 0;
    width: 1200px;
    top: 841px;
    font-size: 62px;
    font-weight: 800;
    text-align: center;
    letter-spacing: -1.5px;
  }
  .body-line {
    left: 0;
    width: 1200px;
    text-align: center;
    font-size: 39px;
    font-weight: 400;
    letter-spacing: -0.3px;
  }
  .body-line--one { top: 938px; }
  .body-line--two { top: 986px; }
  .body-line--three {
    top: 1030px;
    font-size: 50px;
    font-weight: 800;
    letter-spacing: -0.5px;
  }
  .body-line strong { font-weight: 800; }
  .footnote {
    right: 64px;
    top: 1159px;
    font-size: 17px;
    font-weight: 700;
    font-style: italic;
  }
</style>
</head>
<body>
<main class="ad">
  <svg class="ad__backdrop" width="1200" height="1200" viewBox="0 0 1200 1200" aria-hidden="true">
    <rect width="1200" height="1200" fill="var(--yellow)"/>
    <polygon points="0,0 724,0 452,1200 0,1200" fill="var(--teal)"/>
    <rect x="65" y="65" width="1072" height="1072" fill="none" stroke="var(--frame-tint)" stroke-width="14"/>
  </svg>

  <div class="laptop laptop--pc" role="img" aria-label="Silver PC laptop showing a blue Pendrel desktop screen"></div>
  <div class="laptop laptop--zorvane" role="img" aria-label="Zorvane laptop seen from the front with a blue screen"></div>

  <svg class="ribbon" width="1200" height="1200" viewBox="0 0 1200 1200" aria-hidden="true">
    <polygon points="134,634 240,634 240,722 134,722 170,678" fill="var(--red)"/>
    <polygon points="200,694 240,694 240,722" fill="var(--red-dark)"/>
    <polygon points="1066,634 958,634 958,722 1066,722 1030,678" fill="var(--red)"/>
    <polygon points="998,694 958,694 958,722" fill="var(--red-dark)"/>
    <rect x="200" y="606" width="798" height="88" fill="var(--red)"/>
  </svg>
  <p class="ribbon__text">FOR SME BUSINESS ONLY!</p>

  <svg class="chat-icon" width="186" height="106" viewBox="0 0 186 106" aria-hidden="true">
    <path d="M14 2 H96 a12 12 0 0 1 12 12 V50 a12 12 0 0 1 -12 12 H32 L20 76 V62 H14 a12 12 0 0 1 -12 -12 V14 a12 12 0 0 1 12 -12 Z" fill="var(--bubble-grey)"/>
    <path d="M68 18 H168 a14 14 0 0 1 14 14 V78 a14 14 0 0 1 -14 14 H146 L160 106 L126 92 H68 a14 14 0 0 1 -14 -14 V32 a14 14 0 0 1 14 -14 Z" fill="var(--red)"/>
    <circle cx="98" cy="55" r="7" fill="var(--yellow)"/>
    <circle cx="118" cy="55" r="7" fill="var(--yellow)"/>
    <circle cx="138" cy="55" r="7" fill="var(--yellow)"/>
  </svg>

  <h1 class="headline">CHAT WITH US!</h1>
  <p class="body-line body-line--one">TO GET ADVICE ON HOW TO APPLY</p>
  <p class="body-line body-line--two">AND DEFRAY <strong>UP TO 80%</strong>* OF BUSINESS</p>
  <p class="body-line body-line--three">LAPTOP PURCHASE COST!</p>

  <p class="footnote">*Terms and Conditions apply</p>
</main>
</body>
</html>
```